Promotion for Local Garage - KWB Motors offering 10% off

We are after an A5 Colour Leaflet to promote our business KWB Motors.

KWB Motors is a local garage and we are about to launch a flyer campaign in the local area.

Services we provide:
Servicing, Repairs, Diagnostics, Clutches, Brakes, Exhaust for all makes and models of cars and vans.

10% discount for anyone who brings in this flyer with them.

Company contact details below:
Telephone 0151 4938271
Website www.kwbmotors-example.co.uk

Address
Unit 4 Harbour Workshops,
Millbeck Lane,
Glenworth Ind Estate,
Ellesmere Port,
CH65 8QX

Our Logo is attached

Target Market(s)

Local Residents and businesses

Industry/Entity Type

Auto Repair

Requirements
Must have
• Services we provide:
• Servicing, Repairs, Diagnostics, Clutches, Brakes, Exhaust for all makes and models of cars and vans.
• 10% discount for anyone who brings in this flyer with them.
• Company contact details below:
• Telephone 0151 4938271
• Website www.kwbmotors-example.co.uk
• Address
• Unit 4 Harbour Workshops,
• Millbeck Lane,
• Glenworth Ind Estate,
• Ellesmere Port,
• CH65 8QX

```html
<!DOCTYPE html>
<html lang="en">
<head>
<meta charset="utf-8">
<title>KWB Motors – Flyer</title>
<link rel="stylesheet" href="https://fonts.googleapis.com/css2?family=Open+Sans:wdth,wght@75..100,400..800&display=swap">
<style>
  :root {
    --backdrop: #9c9c9c;
    --paper: #ffffff;
    --brand-red: #e21f26;
    --ink: #222222;
    --ink-soft: #3a3a3a;
    --footer: #555555;
    --frame-shadow: #d4d4d4;
    --map: #e4e4e2;
  }
  * { margin: 0; padding: 0; box-sizing: border-box; }
  html, body { width: 800px; height: 1200px; overflow: hidden; background: var(--backdrop); }
  body { position: relative; font-family: "Open Sans", Arial, sans-serif; color: var(--ink); }

  .flyer { position: absolute; left: 65px; top: 123px; width: 672px; height: 955px; background: var(--paper); overflow: hidden; }
  .top-band { position: absolute; left: 0; top: 0; width: 672px; height: 262px; background: var(--brand-red); }
  .top-band::after { content: ""; position: absolute; left: 25px; top: 37px; right: 25px; bottom: 0; background: var(--paper); }

  .hero-photo { position: absolute; left: 25px; top: 42px; width: 622px; height: 380px;
    background: linear-gradient(160deg, #e9ecee 0%, #cfd5da 22%, #7f9ac8 36%, #2f55a8 50%, #27427f 64%, #8d9296 78%, #b7b9ba 100%); }

  .thumb { position: absolute; top: 335px; width: 188px; height: 134px; background: var(--paper); padding: 4px;
    box-shadow: 0 6px 10px var(--frame-shadow); }
  .thumb span { display: block; width: 100%; height: 100%; }
  .thumb--diag { left: 43px; } .thumb--diag span { background: linear-gradient(120deg, #2a3c68 0%, #c79a84 35%, #4a4843 65%, #1f2023 100%); }
  .thumb--engine { left: 246px; } .thumb--engine span { background: linear-gradient(135deg, #1c1e22 0%, #8e9398 40%, #d0d3d6 55%, #303338 100%); }
  .thumb--brake { left: 448px; } .thumb--brake span { background: linear-gradient(135deg, #2a2d31 0%, #6b6e72 35%, #cfcfcd 60%, #9a8f80 80%, #2f3135 100%); }

  .tab { position: absolute; left: 0; background: var(--brand-red); color: #fff; font-weight: 700;
    font-stretch: 80%; border-radius: 0 10px 10px 0; box-shadow: 0 6px 8px rgba(0,0,0,.18); }
  .tab--services { top: 523px; width: 288px; height: 42px; font-size: 25px; line-height: 42px; padding-left: 17px; }
  .tab--contact { top: 776px; width: 203px; height: 32px; font-size: 25px; line-height: 32px; padding-left: 33px; }

  .brand { position: absolute; left: 408px; top: 537px; display: flex; align-items: center; gap: 10px; }
  .brand-dot { width: 14px; height: 14px; border-radius: 50%; background: var(--brand-red); }
  .brand-name { font-size: 28px; font-weight: 600; color: var(--ink-soft); letter-spacing: .5px; }

  .services { position: absolute; left: 25px; top: 590px; width: 620px; list-style: none;
    display: grid; grid-template-columns: 210px 217px 190px; row-gap: 12px; }
  .services li { display: flex; align-items: center; gap: 8px; font-size: 21px; font-weight: 700; line-height: 28px; }
  .services svg { width: 13px; height: 13px; flex: none; }

  .coverage { position: absolute; left: 23px; top: 667px; font-size: 20px; font-weight: 700; letter-spacing: .6px; white-space: nowrap; }

  .offer { position: absolute; left: 15px; top: 705px; display: flex; align-items: center; }
  .offer-amount { font-size: 57px; font-weight: 700; font-stretch: 80%; line-height: 60px; padding-right: 14px; border-right: 2px solid var(--ink); white-space: nowrap; }
  .offer-terms { font-size: 25px; font-weight: 600; font-stretch: 80%; line-height: 27px; padding-left: 18px; white-space: nowrap; }

  .phone { position: absolute; left: 20px; top: 820px; display: flex; align-items: center; gap: 8px; }
  .phone svg { width: 22px; height: 22px; }
  .phone-number { font-size: 43px; font-weight: 700; font-stretch: 85%; line-height: 48px; }

  .address { position: absolute; left: 20px; top: 872px; display: flex; gap: 12px; }
  .address svg { width: 18px; height: 22px; margin-top: 2px; }
  .address p { font-size: 15px; line-height: 20px; color: var(--ink); font-style: normal; }

  .map { position: absolute; left: 392px; top: 780px; width: 256px; height: 128px;
    background: linear-gradient(180deg, #e8e8e6 0%, #e2e2e0 70%, #d4d4d2 100%); }

  .footer { position: absolute; left: 0; top: 921px; width: 672px; height: 34px; background: var(--footer);
    color: #fff; font-size: 21px; text-align: center; line-height: 34px; letter-spacing: 1px; }
</style>
</head>
<body>
  <main class="flyer">
    <div class="top-band"></div>
    <div class="hero-photo" role="img" aria-label="Photo of a garage workshop with a blue people carrier and a blue hatchback raised on lifts"></div>

    <div class="thumb thumb--diag"><span role="img" aria-label="Photo of a mechanic using a diagnostic tool under a bonnet"></span></div>
    <div class="thumb thumb--engine"><span role="img" aria-label="Close-up photo of an engine bay"></span></div>
    <div class="thumb thumb--brake"><span role="img" aria-label="Close-up photo of a brake disc and caliper"></span></div>

    <h2 class="tab tab--services">SERVICES WE PROVIDE</h2>

    <div class="brand"><span class="brand-dot"></span><span class="brand-name">KWB Motors</span></div>

    <ul class="services">
      <li><svg viewBox="0 0 13 13"><rect x=".75" y=".75" width="11.5" height="11.5" fill="none" stroke="#222" stroke-width="1.5"/><path d="M3 6.5l2.5 2.5L10 3.5" fill="none" stroke="#222" stroke-width="1.6"/></svg>SERVICINGS</li>
      <li><svg viewBox="0 0 13 13"><rect x=".75" y=".75" width="11.5" height="11.5" fill="none" stroke="#222" stroke-width="1.5"/><path d="M3 6.5l2.5 2.5L10 3.5" fill="none" stroke="#222" stroke-width="1.6"/></svg>DIAGNOSTIC</li>
      <li><svg viewBox="0 0 13 13"><rect x=".75" y=".75" width="11.5" height="11.5" fill="none" stroke="#222" stroke-width="1.5"/><path d="M3 6.5l2.5 2.5L10 3.5" fill="none" stroke="#222" stroke-width="1.6"/></svg>BRAKES</li>
      <li><svg viewBox="0 0 13 13"><rect x=".75" y=".75" width="11.5" height="11.5" fill="none" stroke="#222" stroke-width="1.5"/><path d="M3 6.5l2.5 2.5L10 3.5" fill="none" stroke="#222" stroke-width="1.6"/></svg>EXHAUST</li>
      <li><svg viewBox="0 0 13 13"><rect x=".75" y=".75" width="11.5" height="11.5" fill="none" stroke="#222" stroke-width="1.5"/><path d="M3 6.5l2.5 2.5L10 3.5" fill="none" stroke="#222" stroke-width="1.6"/></svg>REPAIRS</li>
      <li><svg viewBox="0 0 13 13"><rect x=".75" y=".75" width="11.5" height="11.5" fill="none" stroke="#222" stroke-width="1.5"/><path d="M3 6.5l2.5 2.5L10 3.5" fill="none" stroke="#222" stroke-width="1.6"/></svg>CLUTCHES</li>
    </ul>

    <p class="coverage">FOR ALL MAKES MODELS OF CARS AND VANS</p>

    <div class="offer">
      <p class="offer-amount">10% DISCOUNT</p>
      <p class="offer-terms">FOR ANYONE WHO BRINGS<br>IN THIS FLYER WITH THEM</p>
    </div>

    <h2 class="tab tab--contact">Get In Touch</h2>

    <div class="phone">
      <svg viewBox="0 0 24 24"><path d="M6.6 2.5l3 3.2-1.8 2.6c1 2.4 3.4 4.9 5.9 5.9l2.6-1.8 3.2 3-2.2 3.1C11 18.3 5.7 13 4 6.1z" fill="none" stroke="#222" stroke-width="1.7" stroke-linejoin="round"/><path d="M14 3.5a7 7 0 0 1 6.5 6.5M14 7a3.5 3.5 0 0 1 3 3" fill="none" stroke="#222" stroke-width="1.5"/></svg>
      <p class="phone-number">0151 4938271</p>
    </div>

    <div class="address">
      <svg viewBox="0 0 18 22"><path d="M9 1.5a6 6 0 0 0-6 6c0 4.5 6 11 6 11s6-6.5 6-11a6 6 0 0 0-6-6z" fill="none" stroke="#222" stroke-width="1.7"/><circle cx="9" cy="7.5" r="2.2" fill="none" stroke="#222" stroke-width="1.5"/><path d="M2 20.5h14" stroke="#222" stroke-width="1.7"/></svg>
      <address><p>Unit 4 Harbour Workshops, Millbeck Lane,<br>Glenworth Ind Estate, Ellesmere Port, CH65 8QX</p></address>
    </div>

    <div class="map" role="img" aria-label="Street map showing the workshop location"></div>

    <footer class="footer">www.kwbmotors-example.co.uk</footer>
  </main>
</body>
</html>
```